Dental Office Needs- Flyer Design for Same Day Crowns

We need a flyer that will explain the benefits of the same day crown from the patient prospective. Not show pictures of the machine that makes the crowns. See attached material for content. The flyer should use the practices PMS colors of Green 562 and Blue 3025. The ad should say to the patient - I want to go this office and get my crown done there.
Updates

Project Deadline Extended Reason: The difference in the time zone between USA and Europe has caused issues. Minor changes still need to be worked out. Added Thursday, July 14, 2016

Target Market(s)

Dental Patients

Industry/Entity Type

Dental

Requirements
Must have
• Call to Action
• Business Address and Business Logo
• Classic Design
• images of a Happy 50 year old Couple
• Gives the benefits of the same day crown
Should not have
• No Images of tooth figures
• No before or after pictures

```html
<!DOCTYPE html>
<html lang="en">
<head>
<meta charset="utf-8">
<title>Brookfield Dental Care – Same Day Crowns</title>
<link rel="stylesheet" href="https://fonts.googleapis.com/css2?family=Oswald:wght@300;400;600;700&family=PT+Sans+Narrow:wght@400;700&family=Archivo+Black&display=swap">
<style>
  :root {
    --green: #00806a;
    --blue: #03557d;
    --sky: #a6d8f5;
    --white: #ffffff;
  }
  html, body { margin: 0; padding: 0; overflow: hidden; }
  body { width: 927px; height: 1200px; background: var(--white); }
  .flyer {
    position: relative; width: 927px; height: 1200px; overflow: hidden;
    font-family: "PT Sans Narrow", "Arial Narrow", sans-serif;
  }
  .backdrop { position: absolute; inset: 0; }

  .goodbyes {
    position: absolute; top: 14px; left: 0; width: 927px;
    display: flex; justify-content: space-between; padding: 0 60px 0 70px; box-sizing: border-box;
    color: var(--green); text-align: center;
  }
  .goodbye-word {
    display: block; font-family: "Oswald", sans-serif; font-weight: 700;
    font-size: 50px; line-height: 1.1; letter-spacing: 0.5px;
  }
  .goodbye-item {
    display: block; font-family: "Oswald", sans-serif; font-weight: 300;
    font-size: 25px; line-height: 1.2; letter-spacing: 0.3px; margin-top: 6px;
  }

  .intro {
    position: absolute; left: 40px; top: 598px; width: 360px;
    color: var(--white); font-size: 24px; line-height: 46px; margin: 0;
  }
  .intro strong { font-weight: 700; }
  .intro-offer { top: 783px; font-size: 23px; }

  .brand-card {
    position: absolute; left: 37px; top: 956px; width: 360px; height: 194px;
    background: var(--white); border-radius: 14px;
    display: flex; flex-direction: column; align-items: center; justify-content: center;
    color: var(--blue);
  }
  .brand-name { font-size: 36px; font-weight: 400; letter-spacing: 0.5px; }
  .brand-tagline { font-size: 18px; color: var(--green); margin-top: 6px; }

  .explainer {
    position: absolute; left: 438px; top: 584px; width: 462px; margin: 0;
    color: var(--blue); font-size: 21px; line-height: 49px;
    text-transform: uppercase; text-align: justify;
  }
  .prompt {
    position: absolute; left: 438px; top: 803px; width: 462px; margin: 0;
    color: var(--blue); font-family: "Archivo Black", sans-serif;
    font-size: 19px; line-height: 29px; text-align: center; letter-spacing: 1px;
  }
  .call-box {
    position: absolute; left: 501px; top: 890px; width: 374px; height: 182px;
    background: var(--blue); border-radius: 10px; color: var(--white); text-align: center;
  }
  .call-label { display: block; font-size: 40px; margin-top: 26px; }
  .call-number {
    display: block; font-family: "Oswald", sans-serif; font-weight: 700;
    font-size: 50px; margin-top: 8px; letter-spacing: 0.5px;
  }
  .address {
    position: absolute; left: 574px; top: 1088px; margin: 0;
    color: var(--white); font-size: 27px; line-height: 38px; font-style: normal;
  }
</style>
</head>
<body>
<div class="flyer">
  <svg class="backdrop" width="927" height="1200" viewBox="0 0 927 1200">
    <defs>
      <linearGradient id="photoTone" x1="0" y1="0" x2="1" y2="1">
        <stop offset="0" stop-color="#c9d6a8"/>
        <stop offset="0.35" stop-color="#d9ab8e"/>
        <stop offset="0.7" stop-color="#e6bfa6"/>
        <stop offset="1" stop-color="#cfd9b0"/>
      </linearGradient>
    </defs>
    <rect x="0" y="140" width="927" height="1060" fill="var(--sky)"/>
    <path d="M0,185 C20,270 50,330 80,370 L0,390 Z" fill="var(--green)"/>
    <path d="M927,820 C820,990 620,1060 400,1066 L0,1066 L0,1200 L927,1200 Z" fill="var(--green)"/>
    <path d="M8,262 C50,420 230,540 470,548 C660,550 820,470 927,335 V352 C820,490 650,568 416,576 V1140 Q416,1168 388,1168 H36 Q8,1168 8,1140 Z" fill="var(--blue)"/>
    <g role="img" aria-label="Photo of a smiling couple in their fifties, cheek to cheek, outdoors">
      <path d="M40,140 H927 V322 C820,440 660,510 470,514 C280,516 150,452 105,400 C62,330 40,240 40,140 Z" fill="url(#photoTone)"/>
    </g>
  </svg>

  <header class="goodbyes">
    <div><span class="goodbye-word">GOOD-BYE</span><span class="goodbye-item">TEMPORARY CROWN</span></div>
    <div><span class="goodbye-word">GOOD-BYE</span><span class="goodbye-item">SECOND APPOINTMENT</span></div>
    <div><span class="goodbye-word">GOOD-BYE</span><span class="goodbye-item">GOOEY MESSY IMPRESSIONS</span></div>
  </header>

  <p class="intro">When it comes to your next crown, the benefits of a Digital Restoration add up quickly!</p>
  <p class="intro intro-offer"><strong>Brookfield Dental Care</strong> is pleased to offer you the Comfort and Convenience of One Visit Dental Care.</p>

  <div class="brand-card">
    <span class="brand-name">Brookfield Dental Care</span>
    <span class="brand-tagline">It All Begins With a Healthy Smile!</span>
  </div>

  <p class="explainer">Restorative dentistry has evolved and now, digital technology allows us to take an impression of your teeth with a digital scanner and create your restoration right in our office.</p>

  <p class="prompt">FIND OUT IF DIGITAL DENTISTRY IS RIGHT FOR YOU.</p>

  <div class="call-box">
    <span class="call-label">Call Us Today</span>
    <span class="call-number">248-555-0172</span>
  </div>

  <address class="address">418 W. Lakeview Road,<br>Lakeview, MI</address>
</div>
</body>
</html>
```